Update existing website to a one page design.

Combine a multi page website into a single page design.
Existing site is at ac.tallowmerecover (dot) com.
Rearrange elements as needed to create a modem look.
Not every element / all of the text need to be kept, design should be flexible enough to allow for new text (of different length) to be used.
Site should have a clear calls to action, such as get a quote and contact us.
Ability, call to action, to switch to Russian should be clearly visible near the top, translation will not be done by vextra, thus attribution is not needed.
Unused features (such as blog) should be dropped.
Images, besides logos, can be brand new.
Site should adhere to standard design practices (such as grid) and ideally be compatible with existing framework (such as bootstrap).
Coding of the website will likely be done by the winning bidder as a separate project.

```html
<!DOCTYPE html>
<html lang="en">
<head>
<meta charset="utf-8">
<title>Tallowmere Cover</title>
<link href="https://fonts.googleapis.com/css2?family=Open+Sans:wght@400;600;700&family=Roboto+Condensed:wght@400;700&display=swap" rel="stylesheet">
<style>
:root{
  --blue:#1c4fa1;
  --blue-dark:#163f86;
  --blue-mid:#3d6fbf;
  --blue-soft:#8fb0dc;
  --yellow:#eba21b;
  --yellow-soft:#f5d08a;
  --ink:#222;
  --text:#555;
  --grey-bg:#f3f3f3;
  --line:#dcdcdc;
  --white:#fff;
}
*{box-sizing:border-box;margin:0;padding:0}
html,body{width:1200px;height:5185px;overflow:hidden}
body{font-family:"Open Sans",Arial,sans-serif;color:var(--text);background:var(--white);position:relative}
.abs{position:absolute}
h2.section-title{font-family:"Roboto Condensed",Arial,sans-serif;font-weight:700;color:var(--ink);font-size:34px;text-align:center;position:absolute;left:0;width:1200px}
p{font-size:11px;line-height:1.75}
.btn-yellow{background:var(--yellow);color:#fff;font-weight:700;font-size:11px;text-transform:uppercase;display:flex;align-items:center;justify-content:center;letter-spacing:.3px}
.photo{position:absolute}
.offset-block{position:absolute;background:var(--blue)}

/* header */
.site-header{position:absolute;left:0;top:0;width:1200px;height:105px;background:#fff}
.brand-mark{left:127px;top:10px;width:84px;height:86px;background:var(--blue)}
.brand-name{left:232px;top:18px;font-weight:700;font-size:15px;color:var(--yellow)}
.brand-tag{left:232px;top:38px;font-size:9px;color:#666}
.main-nav{left:302px;top:64px;display:flex;gap:28px;font-size:10.5px;color:#222}
.help{left:838px;top:16px;display:flex;gap:8px;align-items:center}
.help small{display:block;font-size:9px;color:var(--blue)}
.help strong{display:block;font-size:17px;color:var(--blue);font-family:"Roboto Condensed",sans-serif}
.lang{left:1030px;top:26px;display:flex;gap:5px;align-items:center;font-size:9px;color:#333}

/* hero */
.hero-photo{left:0;top:105px;width:1200px;height:540px;background:linear-gradient(100deg,#d9cbb7 0%,#efe4d6 45%,#cfdbe6 100%)}
.quote-panel{left:760px;top:110px;width:277px}
.qp-top{height:62px;background:var(--blue);color:#fff;font-size:19px;display:flex;align-items:center;justify-content:center}
.qp-band{height:74px;background:var(--blue-mid);color:#fff;font-size:20px;font-weight:600;text-align:center;line-height:1.3;padding-top:10px}
.qp-body{height:186px;background:var(--blue);color:#fff;text-align:center;padding:20px 30px 0}
.qp-body p{font-size:11.5px;line-height:1.7}
.qp-select{margin:18px auto 0;width:212px;height:38px;background:#fff;color:#666;font-size:10px;display:flex;align-items:center;justify-content:space-between;padding:0 14px}
.group-panel{left:760px;top:442px;width:277px;height:125px;background:var(--yellow);color:#fff;padding:16px 20px}
.group-panel h3{font-family:"Roboto Condensed",sans-serif;font-size:19px;font-weight:700}
.group-panel small{font-size:11px;display:block;margin-top:2px}
.gp-btn{margin-top:14px;width:165px;height:34px;border:1px solid #fff;font-size:10px;font-weight:700;display:flex;align-items:center;justify-content:center}

/* carriers */
.carriers-title{left:0;top:688px;width:1200px;text-align:center;font-family:"Roboto Condensed",sans-serif;font-weight:700;font-size:13px;color:#222}
.carrier{top:728px;height:82px;background:#fff;box-shadow:0 2px 8px rgba(0,0,0,.12);display:flex;align-items:center;justify-content:center;font-weight:700;font-size:18px;color:var(--ink)}
.carrier.active{border:2px solid #9ab3db}
.arrow{top:756px;width:28px;height:28px;border-radius:50%;background:#eef2f8;display:flex;align-items:center;justify-content:center}

/* about */
.about{left:0;top:855px;width:1200px;height:535px;background:var(--grey-bg)}
.about-text{left:161px;top:130px;width:440px}
.about-text p{margin-bottom:12px}
.about-text p.lead{color:#333}

/* individual */
.options-head{left:0;width:1200px;text-align:center}
.opt{position:absolute;width:345px}
.opt .icon{position:absolute;left:-50px;top:0}
.opt h4{font-size:13.5px;color:#222;font-weight:600;margin-bottom:4px}
.opt p{font-size:10px;line-height:1.7}

/* group */
.group{left:0;top:2047px;width:1200px;height:378px;background:var(--blue)}
.group h2{color:#fff!important}
.gcard{top:127px;width:362px;height:188px;background:#fff;padding:18px 22px}
.gcard h3{font-weight:400;font-size:23px;color:var(--yellow);margin-bottom:8px}
.gcard p{font-size:10px;line-height:1.8}
.readmore{font-size:10px;color:#333;text-decoration:underline}

/* life */
.life-sub{left:181px;top:2560px;font-size:14px;color:var(--yellow)}
.life-list{display:grid;grid-template-columns:140px 140px;row-gap:16px;font-size:11px;color:#333}
.life-list span::before{content:"";display:inline-block;width:6px;height:6px;border-radius:50%;background:var(--yellow);margin-right:10px;vertical-align:middle}

/* pension */
.pension{left:0;top:2875px;width:600px;height:310px;background:var(--blue-soft);padding:38px 34px 0 165px}
.annuity{left:600px;top:2875px;width:600px;height:310px;background:var(--yellow-soft);padding:38px 165px 0 34px}
.pension h3,.annuity h3{font-family:"Roboto Condensed",sans-serif;font-size:30px;color:#111;margin-bottom:16px}
.pension p,.annuity p{font-size:9.6px;line-height:1.8;color:#333;margin-bottom:10px}

/* property */
.pcard{top:3321px;width:262px}
.pcard .img{height:168px}
.pcard h4{font-weight:400;font-size:16px;color:var(--yellow);margin:14px 0 6px 6px}
.pcard p{font-size:10px;line-height:1.7;margin-left:6px}
.pcard .readmore{margin-left:6px;display:inline-block;margin-top:8px}

/* services */
.services-list{left:222px;top:3827px;list-style:none}
.services-list li{font-size:13px;font-weight:600;color:#333;height:30.7px;display:flex;align-items:center;gap:10px}

/* doctors */
.doctor{top:4380px;font-weight:700;font-size:22px;color:var(--ink)}

/* contact */
.contact{left:0;top:4473px;width:1200px;height:439px;background:linear-gradient(120deg,#122a52,#1c3c73 60%,#16315f)}
.contact h3{position:absolute;left:163px;top:125px;width:420px;font-family:"Roboto Condensed",sans-serif;font-weight:400;font-size:27px;line-height:1.4;color:#fff}
.census{left:663px;top:4473px;width:374px;height:579px;background:var(--blue);padding:28px 36px 0;color:#fff}
.census small{display:block;text-align:center;font-size:10px;letter-spacing:2px;font-weight:700}
.census h3{text-align:center;font-family:"Roboto Condensed",sans-serif;font-weight:400;font-size:30px;margin-bottom:18px}
.field{background:#fff;color:#888;font-size:9px;height:36px;padding:10px 12px;margin-bottom:8px}
.row2{display:flex;gap:8px}.row2 .field{flex:1}
.checks{display:flex;gap:16px;font-size:10px;margin:6px 0 18px}
.checks span::before{content:"";display:inline-block;width:9px;height:9px;border:1px solid #fff;margin-right:5px;vertical-align:middle}
.submit{height:38px;margin-top:16px}

/* footer */
.footer-brand{left:169px;top:4930px}
.foot-mark{width:62px;height:62px;background:var(--blue)}
.footer-links{font-size:10px;color:#222;line-height:28px}
.copyright{left:0;top:5162px;width:1200px;text-align:center;font-size:9px;color:#666;border-top:1px solid var(--line);padding-top:6px}
</style>
</head>
<body>

<header class="site-header">
  <div class="abs brand-mark"></div>
  <div class="abs brand-name">TallowmereCover.com</div>
  <div class="abs brand-tag">Think of your future, think Tallowmere Cover!</div>
  <nav class="abs main-nav">
    <span>Home</span><span>Individual Health</span><span>Group Health</span><span>Life Insurance</span><span>Pension &amp; Annuities</span><span>Property &amp; Commercia</span><span>Doctors Network</span><span>Contact us</span>
  </nav>
  <div class="abs help">
    <svg width="30" height="30" viewBox="0 0 30 30"><circle cx="15" cy="15" r="13" fill="none" stroke="#eba21b" stroke-width="2"/><path d="M10 9l3 0 1 4-2 1c1 2 2 3 4 4l1-2 4 1v3c-6 0-11-5-11-11z" fill="#eba21b"/></svg>
    <div><small>Our experts are here to help</small><strong>877-555-0142</strong></div>
  </div>
  <div class="abs lang">
    <svg width="14" height="12"><rect width="14" height="4" fill="#fff" stroke="#ddd" stroke-width=".5"/><rect y="4" width="14" height="4" fill="#2a52be"/><rect y="8" width="14" height="4" fill="#d52b1e"/></svg>
    <span>RU</span>
    <svg width="8" height="6"><path d="M1 1l3 3 3-3" stroke="#333" fill="none"/></svg>
  </div>
</header>

<div class="photo hero-photo" role="img" aria-label="Smiling multi-generation family on a bright beach"></div>
<div class="abs quote-panel">
  <div class="qp-top">Click Here To Get An</div>
  <div class="qp-band">Individual Health<br>Insurance Quote</div>
  <div class="qp-body">
    <p>Shop Online for an affordable individual &amp; Family Health Insurance Plan. All Major Companies represented.</p>
    <div class="qp-select"><span>Select Your Carriers</span><svg width="9" height="6"><path d="M1 1l3.5 3.5 3.5-3.5" stroke="#333" fill="none"/></svg></div>
  </div>
</div>
<div class="abs group-panel">
  <h3>CLICK HERE TO GET AN</h3>
  <small>GROUP HEALTH INSURANCE QUOTE</small>
  <div class="gp-btn">GET A QUOTE</div>
</div>

<div class="abs carriers-title">YOUR SATISFACTION IS OUR REWARD.</div>
<div class="abs arrow" style="left:178px"><svg width="8" height="10"><path d="M6 1L2 5l4 4" stroke="#1c4fa1" fill="none" stroke-width="1.5"/></svg></div>
<div class="abs carrier" style="left:238px;width:120px">Brennoch</div>
<div class="abs carrier active" style="left:429px;width:149px">Rovalis</div>
<div class="abs carrier" style="left:624px;width:131px">Tessmont</div>
<div class="abs carrier" style="left:811px;width:151px">Quillgate</div>
<div class="abs arrow" style="left:993px"><svg width="8" height="10"><path d="M2 1l4 4-4 4" stroke="#1c4fa1" fill="none" stroke-width="1.5"/></svg></div>

<section class="abs about">
  <h2 class="section-title" style="top:52px">Tallowmere Cover Insurance</h2>
  <div class="abs about-text">
    <p class="lead">Tallowmere Cover Corporation is an Independent Insurance and Financial Brokerage Firm serving clients throughout Florida and Internationally. We are an experienced team of professionals, committed to our primary mission – to find the less expensive insurance coverage, for protection you want, at the best rate you deserve.</p>
    <p>Our integrated suite of online services facilitates a comprehensive search and review of leading insurance companies.</p>
    <p>Tallowmere Cover Corporation is not owned by any insurance company, therefore we provide objective information to consumers and small business owners, helping them make informed decisions about their insurance and financial needs. We aim to offer you the highest quality insurance and service on the market.</p>
    <div class="btn-yellow" style="width:300px;height:40px;margin-top:22px">GET AN GROUP HEALTH INSURANCE QUOTE</div>
  </div>
  <div class="offset-block" style="left:723px;top:190px;width:344px;height:238px"></div>
  <div class="photo" style="left:636px;top:131px;width:401px;height:278px;background:linear-gradient(160deg,#6f9a4a,#a7c47a 50%,#3f6b2d)" role="img" aria-label="Family walking together in a sunny park"></div>
</section>

<h2 class="section-title" style="top:1440px">Individual Health &amp; Individual Medical Insurance</h2>
<div class="abs options-head" style="top:1518px;font-size:18px;color:#444">Health Options</div>
<div class="abs options-head" style="top:1543px;font-size:14px;color:var(--yellow)">Coverage options include:</div>

<div class="opt" style="left:227px;top:1594px">
  <svg class="icon" width="28" height="28"><rect x="3" y="3" width="22" height="22" rx="3" fill="none" stroke="#eba21b" stroke-width="1.8"/><path d="M9 14h10M14 9v10" stroke="#eba21b" stroke-width="1.8"/></svg>
  <h4>Major Medical</h4><p>Provides benefits for most types of medical expenses. PPO, HMO, POS, HSA and Traditional comprehensive policies remain the industry standard, while the supplemental offerings are highly recommended to fill the gaps.</p>
</div>
<div class="opt" style="left:227px;top:1703px">
  <svg class="icon" width="28" height="28"><rect x="3" y="3" width="22" height="22" rx="3" fill="none" stroke="#eba21b" stroke-width="1.8"/><path d="M9 14h10M14 9v10" stroke="#eba21b" stroke-width="1.8"/></svg>
  <h4>Dental Insurance:</h4><p>For quality and affordable dental care we offer rich plans and unbeatable savings with the security of knowing that you will be protected from hidden fees and surprises. PPO and HMO plans are available.</p>
</div>
<div class="opt" style="left:227px;top:1815px">
  <svg class="icon" width="28" height="28"><rect x="3" y="3" width="22" height="22" rx="3" fill="none" stroke="#eba21b" stroke-width="1.8"/><path d="M9 14h10M14 9v10" stroke="#eba21b" stroke-width="1.8"/></svg>
  <h4>Health Insurance for Foreign Nationals</h4><p>Whether you are visiting or immigrating, whatever your status, insurance policies are available to cover your stay in the US, or to cover your transition from your home country to ours.</p>
</div>
<div class="opt" style="left:227px;top:1910px">
  <svg class="icon" width="28" height="28"><rect x="3" y="3" width="22" height="22" rx="3" fill="none" stroke="#eba21b" stroke-width="1.8"/><path d="M9 14h10M14 9v10" stroke="#eba21b" stroke-width="1.8"/></svg>
  <h4>Disability Income Insuranc</h4><p>Protection for when you can't work because of illness or injury. Policies specify how, when and for what duration benefits are paid, and how much pay you will receive while out of work.</p>
</div>
<div class="opt" style="left:701px;top:1594px">
  <svg class="icon" width="28" height="28"><circle cx="14" cy="14" r="11" fill="none" stroke="#eba21b" stroke-width="1.8"/><path d="M3 14h22M14 3c5 5 5 17 0 22M14 3c-5 5-5 17 0 22" stroke="#eba21b" fill="none" stroke-width="1.4"/></svg>
  <h4>Worldwide Health Insurance</h4><p>The other side of the equation. Most US insurers (HMO's, PPO's or Medicare) do not adequately provide for international travel medical emergencies or cover more basic visitor medical needs. We have experience in this arena.</p>
</div>
<div class="opt" style="left:701px;top:1703px">
  <svg class="icon" width="28" height="28"><rect x="3" y="3" width="22" height="22" rx="3" fill="none" stroke="#eba21b" stroke-width="1.8"/><path d="M8 10h12M8 14h12M8 18h8" stroke="#eba21b" stroke-width="1.8"/></svg>
  <h4>Medicare Supplements</h4><p>Better known in Florida as Medigap, these plans are designed to cover any gaps between the total amount charged and the amount covered by Medicare. A-J types to choose from.</p>
</div>
<div class="opt" style="left:701px;top:1796px">
  <svg class="icon" width="28" height="28"><rect x="3" y="3" width="22" height="22" rx="3" fill="none" stroke="#eba21b" stroke-width="1.8"/><path d="M8 10h12M8 14h12M8 18h8" stroke="#eba21b" stroke-width="1.8"/></svg>
  <h4>Medicare Advantage Plans</h4><p>A type of health plan where your private insurer contracts with Medicare to provide all your Part A and Part B benefits. Also known as Part C or MA Plans, they must follow the Medicare rules.</p>
</div>
<div class="opt" style="left:701px;top:1886px">
  <svg class="icon" width="28" height="28"><rect x="3" y="3" width="22" height="22" rx="3" fill="none" stroke="#eba21b" stroke-width="1.8"/><path d="M8 10h12M8 14h12M8 18h8" stroke="#eba21b" stroke-width="1.8"/></svg>
  <h4>Long Term Care Insurance (LTCI) and Critical Illness Insurance</h4><p>We will weigh the deciding factors together with you. Age, gender, marital status and lifestyle go into the calculation, along with your family health history. Vital for some; too costly for others.</p>
</div>

<section class="abs group">
  <h2 class="section-title" style="top:40px">Group Health Insurance / Group Medical Insurance</h2>
  <div class="abs gcard" style="left:209px">
    <h3>Then</h3><p>There was a time in generations past when simply holding down a full-time position with your community employer meant having the medical benefits you needed. Such was the nature of the social contract that came with the job. Health insurance and medical services for the most part were available, accessible and affordable.</p>
    <span class="readmore">Read more..</span>
  </div>
  <div class="abs gcard" style="left:628px">
    <h3>Now</h3><p>Today, health insurance is THE topic of conversation nationwide, as it impacts everyone in the workplace. Benefits have often been erased as companies can't keep up with the overall cost. As health reform continues through 2014, we invite you to bring us your questions and concerns.</p>
    <span class="readmore">Read more..</span>
  </div>
</section>

<h2 class="section-title" style="top:2482px">Life Insurance</h2>
<div class="abs life-sub">Life Insurance / Whole Life Insurance / Term Insurance</div>
<p class="abs" style="left:181px;top:2585px;width:380px;font-size:10px">We are specialists in all types of Life Insurance in all of Florida and even internationally. Consider these safety net vehicles as a vital piece of your long-term insurance strategy and estate planning. We will find the options that are the best fits for you from which to choose:</p>
<div class="abs" style="left:181px;top:2680px;font-size:16px;color:#444">Life Insurance Options:</div>
<div class="abs life-list" style="left:183px;top:2716px"><span>Permanent Life</span><span>Universal Life</span><span>Whole Life</span><span>Term Life</span></div>
<div class="offset-block" style="left:694px;top:2617px;width:373px;height:195px"></div>
<div class="photo" style="left:660px;top:2560px;width:377px;height:222px;background:linear-gradient(150deg,#c8b59a,#e9ded0 50%,#9d8a73)" role="img" aria-label="Couple reviewing insurance documents with an advisor"></div>

<section class="abs pension">
  <h3>PENSION</h3>
  <p>Pension is often referred as Individual Retirement Account, known as IRA. It is an investing tool used by individuals to earn and earmark funds for retirement savings. There are several types of IRAs: Traditional IRAs, Roth IRAs, SIMPLE IRAs and SEP IRAs.</p>
  <p>Traditional and Roth IRAs are established by individual taxpayers, who are allowed to contribute 100% of compensation (self-employment income for sole proprietors and partners) up to a set maximum dollar amount. Contributions to the Traditional IRA may be tax-deductible depending on the taxpayer's income, tax-filing status and coverage by an employer-sponsored retirement plan. Roth IRA contributions are not tax-deductible.</p>
</section>
<section class="abs annuity">
  <h3>ANNUITIES</h3>
  <p>An Annuity is a contract between a purchaser and an insurance company in which the insurance company promises to make lifetime periodic payments to the purchaser, starting immediately (Immediate Annuity) or at some time in the future (Deferred Annuity). To set up an annuity, our clients usually use money from their Savings Account, Mutual Funds, CDs, Stocks and Bonds. The annuity may also be funded by existing IRA, 401(k), 403(b), Keogh or HR-10.</p>
  <p>The greatest single factor that motivates people to buy either deferred or immediate annuities is their need for guaranteed retirement income, which will last for the person lifetime.</p>
</section>

<h2 class="section-title" style="top:3238px">Property &amp; Casualty Insurance</h2>
<div class="abs pcard" style="left:161px">
  <div class="img" style="background:linear-gradient(170deg,#9fc1e3,#c79a74 55%,#4d6b3c)" role="img" aria-label="Mediterranean style house with palm trees"></div>
  <h4>Homeowners Insurance</h4><p>Most South Florida residents love it here for our year-round tropical climate, and have long recognized owning a home as part of the Sunshine State's enviable lifestyle.</p><span class="readmore">Read more..</span>
</div>
<div class="abs pcard" style="left:469px">
  <div class="img" style="background:linear-gradient(180deg,#7a6a4f,#c9a865 50%,#6c5a3e)" role="img" aria-label="Warehouse interior with stocked shelves"></div>
  <h4>Commercial Insurance</h4><p>In today's world of legally complex responsibilities, every company (and its owners) is always vulnerable to business-ending liability.</p><span class="readmore">Read more..</span>
</div>
<div class="abs pcard" style="left:777px">
  <div class="img" style="background:linear-gradient(180deg,#2b2f36,#8a9098 55%,#dfe2e6)" role="img" aria-label="White sports car on a dark background"></div>
  <h4>Automobile Insurance</h4><p>Whether on the road or on the waves, we Floridians take pride in how we get around – and how we treat our rides!</p><span class="readmore">Read more..</span>
</div>

<h2 class="section-title" style="top:3737px">Our Services</h2>
<ul class="abs services-list">
  <li><svg width="14" height="14"><circle cx="7" cy="7" r="7" fill="#eba21b"/><path d="M4 7l2 2 4-4" stroke="#fff" stroke-width="1.6" fill="none"/></svg>Auto</li>
  <li><svg width="14" height="14"><circle cx="7" cy="7" r="7" fill="#eba21b"/><path d="M4 7l2 2 4-4" stroke="#fff" stroke-width="1.6" fill="none"/></svg>Commercial</li>
  <li><svg width="14" height="14"><circle cx="7" cy="7" r="7" fill="#eba21b"/><path d="M4 7l2 2 4-4" stroke="#fff" stroke-width="1.6" fill="none"/></svg>Dental Insurance</li>
  <li><svg width="14" height="14"><circle cx="7" cy="7" r="7" fill="#eba21b"/><path d="M4 7l2 2 4-4" stroke="#fff" stroke-width="1.6" fill="none"/></svg>Disability</li>
  <li><svg width="14" height="14"><circle cx="7" cy="7" r="7" fill="#eba21b"/><path d="M4 7l2 2 4-4" stroke="#fff" stroke-width="1.6" fill="none"/></svg>Group Health Insurance</li>
  <li><svg width="14" height="14"><circle cx="7" cy="7" r="7" fill="#eba21b"/><path d="M4 7l2 2 4-4" stroke="#fff" stroke-width="1.6" fill="none"/></svg>Homeowners</li>
  <li><svg width="14" height="14"><circle cx="7" cy="7" r="7" fill="#eba21b"/><path d="M4 7l2 2 4-4" stroke="#fff" stroke-width="1.6" fill="none"/></svg>Individual/Family Health Insurance</li>
  <li><svg width="14" height="14"><circle cx="7" cy="7" r="7" fill="#eba21b"/><path d="M4 7l2 2 4-4" stroke="#fff" stroke-width="1.6" fill="none"/></svg>Medicare Supplements</li>
  <li><svg width="14" height="14"><circle cx="7" cy="7" r="7" fill="#eba21b"/><path d="M4 7l2 2 4-4" stroke="#fff" stroke-width="1.6" fill="none"/></svg>Medicare Advantage Plans</li>
  <li><svg width="14" height="14"><circle cx="7" cy="7" r="7" fill="#eba21b"/><path d="M4 7l2 2 4-4" stroke="#fff" stroke-width="1.6" fill="none"/></svg>Pension &amp; Annuities</li>
  <li><svg width="14" height="14"><circle cx="7" cy="7" r="7" fill="#eba21b"/><path d="M4 7l2 2 4-4" stroke="#fff" stroke-width="1.6" fill="none"/></svg>Long Term Care</li>
</ul>
<div class="offset-block" style="left:628px;top:3895px;width:382px;height:232px"></div>
<div class="photo" style="left:592px;top:3809px;width:374px;height:278px;background:linear-gradient(160deg,#dfe6ec,#aab7c2 50%,#4c5866)" role="img" aria-label="Two businessmen talking in a bright office"></div>

<h2 class="section-title" style="top:4271px">Doctors Network</h2>
<div class="abs doctor" style="left:163px">Rovalis</div>
<div class="abs doctor" style="left:292px">Dunmere</div>
<div class="abs doctor" style="left:448px">Sarvine</div>
<div class="abs doctor" style="left:634px">Quillgate</div>
<div class="abs doctor" style="left:785px">Penwick</div>
<div class="abs doctor" style="left:930px">Ostrel</div>

<section class="abs contact" role="img" aria-label="Dark blue toned photo of a client consultation">
  <h3>We listen to our clients and are happy to discuss any issues or concerns you may have with your policy.</h3>
  <div class="abs btn-yellow" style="left:163px;top:305px;width:286px;height:40px">GET AN INSTANT QUOTE</div>
</section>
<form class="abs census">
  <small>CONTACT US</small>
  <h3>Group Census Form</h3>
  <div class="row2"><div class="field">Name</div><div class="field"></div></div>
  <div class="field">Company Name</div>
  <div class="field">Email</div>
  <div class="field" style="height:76px">Address</div>
  <div style="font-size:10px;margin-top:16px">Are you interested in other products?</div>
  <div class="checks"><span>Life</span><span>Dental</span><span>LTD</span></div>
  <div class="field">Type of Business</div>
  <div class="field">Number of Employees</div>
  <div class="btn-yellow submit">SUBMIT CENSUS</div>
</form>

<footer>
  <div class="abs footer-brand" style="display:flex;gap:12px">
    <div class="foot-mark"></div>
    <div style="padding-top:12px"><div style="font-weight:700;font-size:15px;color:var(--yellow)">TallowmereCover.com</div><div style="font-size:9px;color:#666">Think of your future, think Tallowmere Cover!</div></div>
  </div>
  <div class="abs" style="left:169px;top:5005px;font-size:9px;color:var(--blue)">Friendline</div>
  <div class="abs" style="left:169px;top:5052px;font-size:10px;font-weight:600;color:#222">Tallowmere Cover</div>
  <div class="abs" style="left:169px;top:5072px;display:flex;gap:6px;font-size:9px;line-height:1.5;color:#444">
    <svg width="10" height="13"><path d="M5 12C1 7 1 5 1 5a4 4 0 018 0s0 2-4 7z" fill="#1c4fa1"/></svg>
    <span>412 Harbor Crest Way<br>Suite 210<br>Palm Lantern, FL 33100</span>
  </div>
  <div class="abs" style="left:355px;top:5072px;font-size:9px;color:#444;line-height:2.6">
    <div>☏ 954-555-0187</div><div>✉ info@tallowmerecover.com</div>
  </div>
  <div class="abs footer-links" style="left:560px;top:4925px">Home<br>Who We Are<br>Contact Us<br>Services<br>Doctors Network<br>Group Health<br>Life Insurance</div>
  <div class="abs footer-links" style="left:680px;top:5065px">Pension &amp; Annuities<br>Property &amp; Commercial</div>
  <div class="abs copyright">© 2021 Tallowmere Cover Insurance. All rights Reserved.</div>
</footer>

</body>
</html>
```